Halvern Crest Training PowerPoint Template

I want to PowerPoint template theme using my attached logo. My colors are black and orange. My website is HalvernCrest.com. I am a handgun training company.

Font:

- Serpentine-Bold-Bold for "DORN VALE"

- BrowalliaUPC for "SHOOTING SPORTS"

Colors (CMYK code):

- BLACK ....... 0; 0; 0; 100;
- ORANGE ... gradient from 0; 65; 97.5; 0 to 0; 39; 97.5; 0

```html
<!DOCTYPE html>
<html lang="en">
<head>
<meta charset="UTF-8">
<title>Halvern Crest Training – Slide Template</title>
<link href="https://fonts.googleapis.com/css2?family=Russo+One&family=Arimo:wght@400;700&display=swap" rel="stylesheet">
<style>
  :root {
    --page-bg: #f7f8fa;
    --header-bg: #ffffff;
    --rule: #e6e7e9;
    --ink: #111111;
    --title-ink: #1a1a1a;
    --placeholder: #e0e1e0;
    --footer-bg: #15191d;
    --footer-ink: #ffffff;
    --orange-deep: #f25a06;
    --orange-light: #f79c06;
  }
  * { margin: 0; padding: 0; box-sizing: border-box; }
  html, body { width: 1200px; height: 900px; overflow: hidden; }
  body { background: var(--page-bg); font-family: "Arimo", Arial, sans-serif; color: var(--ink); }
  .slide { position: relative; width: 1200px; height: 900px; background: var(--page-bg); }

  .slide-header {
    position: absolute; left: 0; top: 0; width: 1200px; height: 101px;
    background: var(--header-bg); border-bottom: 2px solid var(--rule);
  }
  .slide-title {
    position: absolute; left: 36px; top: 38px;
    font-family: "Russo One", "Arial Black", sans-serif;
    font-size: 40px; line-height: 1; letter-spacing: 1px; color: var(--title-ink);
  }
  .brand {
    position: absolute; right: 18px; top: 14px; height: 72px;
    display: flex; align-items: center; gap: 14px;
  }
  .brand-mark {
    width: 64px; height: 64px; border-radius: 6px;
    background: linear-gradient(180deg, var(--orange-deep), var(--orange-light));
  }
  .brand-name {
    font-family: "Arimo", Arial, sans-serif; font-weight: 700;
    font-size: 29px; line-height: 1.08; color: var(--ink); letter-spacing: 0.5px;
    text-transform: uppercase;
  }

  .content-row { position: absolute; left: 52px; width: 1114px; }
  .content-row.first { top: 177px; }
  .content-row.second { top: 482px; }
  .body-copy {
    position: absolute; left: 0; top: 0;
    font-size: 22px; line-height: 39px; color: var(--ink);
  }
  .media-slot {
    position: absolute; left: 700px; top: 0; width: 414px; height: 214px;
    background: var(--placeholder); border-radius: 5px;
  }

  .slide-footer {
    position: absolute; left: 0; bottom: 0; width: 1200px; height: 63px;
    background: var(--footer-bg);
    display: flex; align-items: center; justify-content: space-between;
    padding: 0 21px; color: var(--footer-ink);
    font-family: "Arimo", Arial, sans-serif;
  }
  .copyright { font-size: 19px; letter-spacing: 0.3px; }
  .page-number { font-size: 22px; font-weight: 700; padding-right: 3px; }
</style>
</head>
<body>
  <main class="slide">
    <header class="slide-header">
      <h1 class="slide-title">PROJECT TITLE HERE</h1>
      <div class="brand">
        <span class="brand-mark" aria-hidden="true"></span>
        <span class="brand-name">Halvern Crest<br>Training</span>
      </div>
    </header>

    <section class="content-row first">
      <p class="body-copy">
        Lorem ipsum daolor sit ipsum Lorem ipsum dolor sit ipsum<br>
        Lorem ipsum dolor sit ipsum Lorem ipsum dolor sit ipsum<br>
        Lorem ipsum daolor sit ipsum Lorem ipsum dolor sit ipsum<br>
        Lorem ipsum dolor sit ipsum Lorem ipsum dolor sit ipsum<br>
        Lorem ipsum daolor sit ipsum Lorem ipsum dolor sit ipsum<br>
        Lorem ipsum dolor sit ipsum
      </p>
      <div class="media-slot" role="img" aria-label="Image placeholder"></div>
    </section>

    <section class="content-row second">
      <p class="body-copy">
        Lorem ipsum daolor sit ipsum Lorem ipsum dolor sit ipsum<br>
        Lorem ipsum dolor sit ipsum Lorem ipsum dolor sit ipsum<br>
        Lorem ipsum daolor sit ipsum Lorem ipsum dolor sit ipsum<br>
        Lorem ipsum dolor sit ipsum Lorem ipsum dolor sit ipsum<br>
        Lorem ipsum daolor sit ipsum Lorem ipsum dolor sit ipsum<br>
        Lorem ipsum dolor sit ipsum
      </p>
      <div class="media-slot" role="img" aria-label="Image placeholder"></div>
    </section>

    <footer class="slide-footer">
      <span class="copyright">COPYRIGHT TEXT HERE</span>
      <span class="page-number">1</span>
    </footer>
  </main>
</body>
</html>
```